Velmora Homecare - Website

MUST HAVE EXPERIENCE DESIGNING WEBSITES HEALTH CARE IN GENERAL AND/OR HOME NURSING SERVICES.

Details attached.

Number of Pages Required

1 page

Requirements
Must have
• Warm feel
caregivers

Color similar to the logo...

```html
<!DOCTYPE html>
<html lang="en">
<head>
<meta charset="utf-8">
<title>Velmora Homecare</title>
<link href="https://fonts.googleapis.com/css2?family=Montserrat:wght@400;500;600;700&family=Barlow+Condensed:wght@400&family=Comfortaa:wght@400;700&display=swap" rel="stylesheet">
<style>
  :root {
    --teal: #12a0ab;
    --teal-dark: #1c8f98;
    --orange: #f7870f;
    --ink: #1f3b40;
    --white: #ffffff;
    --hero-light: #eef2f6;
  }
  * { margin: 0; padding: 0; box-sizing: border-box; }
  html, body { width: 1200px; height: 902px; overflow: hidden; background: var(--white); }
  body { position: relative; font-family: 'Montserrat', sans-serif; }

  .notice-bar {
    position: absolute; left: 0; top: 0; width: 1200px; height: 50px;
    background: var(--teal); color: var(--white);
    font-weight: 600; font-size: 13.5px; letter-spacing: 0.5px;
    display: flex; align-items: center; justify-content: center;
  }

  .utility-bar {
    position: absolute; left: 0; top: 52px; width: 1200px; height: 66px;
    background: var(--orange); color: var(--white);
  }
  .icon-box {
    position: absolute; width: 33px; height: 33px; top: 16px;
    border: 2px solid var(--white);
    display: flex; align-items: center; justify-content: center;
  }
  .util-item { position: absolute; top: 17px; }
  .util-label { font-size: 12.5px; font-weight: 400; line-height: 16px; }
  .util-value { font-size: 16px; font-weight: 600; letter-spacing: 1px; line-height: 20px; }
  .util-links {
    position: absolute; left: 808px; top: 25px;
    font-size: 13.5px; font-weight: 700; letter-spacing: 0.5px;
  }
  .util-links .sep { margin: 0 11px; }

  .site-header { position: absolute; left: 0; top: 118px; width: 1200px; height: 123px; }
  .brand {
    position: absolute; left: 60px; top: 44px;
    display: flex; align-items: center; gap: 10px;
    color: var(--teal); font-weight: 700; font-size: 22px; letter-spacing: 1px;
  }
  .brand-mark { width: 18px; height: 18px; background: var(--orange); }
  .main-nav {
    position: absolute; right: 87px; top: 55px;
    color: var(--teal); font-weight: 600; font-size: 13.5px; letter-spacing: 0.5px;
    display: flex; gap: 0;
  }
  .main-nav .sep { margin: 0 14px; }

  .hero {
    position: absolute; left: 0; top: 241px; width: 1200px; height: 407px;
    background: linear-gradient(90deg, #e9eef3 0%, #f2f5f8 30%, #eef1f5 100%);
  }
  .hero-photo {
    position: absolute; left: 500px; top: 0; width: 678px; height: 405px;
    background: linear-gradient(90deg, rgba(238,241,245,0) 0%, #d9cfc6 25%, #cfe3df 60%, #7fc8c0 80%, #e6e9ee 100%);
  }
  .hero-title {
    position: absolute; left: 77px; top: 48px;
    font-family: 'Barlow Condensed', sans-serif; color: var(--teal); font-weight: 400;
  }
  .hero-title .line1 { font-size: 54px; line-height: 56px; display: block; }
  .hero-title .line2 { font-size: 42px; line-height: 48px; display: block; }
  .hero-title .line3 {
    font-family: 'Comfortaa', sans-serif; font-weight: 700; color: var(--orange);
    font-size: 68px; line-height: 76px; display: block; letter-spacing: -1px;
  }
  .hero-sub {
    position: absolute; left: 77px; top: 228px;
    font-family: 'Comfortaa', sans-serif; color: var(--ink); font-size: 18px; line-height: 24px;
  }
  .hero-button {
    position: absolute; left: 79px; top: 307px; width: 226px; height: 47px;
    background: var(--white); border: 2px solid #e7ecef;
    display: flex; align-items: center; justify-content: center;
    color: var(--ink); font-weight: 500; font-size: 14.5px; letter-spacing: 0.5px;
  }
</style>
</head>
<body>
  <div class="notice-bar">COVID-19 UPDATE, CLICK HERE TO KNOW ALL DETAILS</div>

  <div class="utility-bar">
    <div class="icon-box" style="left:92px">
      <svg width="14" height="14" viewBox="0 0 24 24"><path fill="#fff" d="M6.6 10.8c1.4 2.8 3.8 5.1 6.6 6.6l2.2-2.2c.3-.3.7-.4 1-.2 1.1.4 2.3.6 3.6.6.6 0 1 .4 1 1V20c0 .6-.4 1-1 1C10.6 21 3 13.4 3 4c0-.6.4-1 1-1h3.5c.6 0 1 .4 1 1 0 1.3.2 2.5.6 3.6.1.3 0 .7-.2 1z"/></svg>
    </div>
    <div class="util-item" style="left:139px">
      <div class="util-label">24/7 service Avaialble</div>
      <div class="util-value">888 555 0199 2040</div>
    </div>
    <div class="icon-box" style="left:347px">
      <svg width="14" height="14" viewBox="0 0 24 24"><path fill="#fff" d="M10 3h4v8h4l-6 6-6-6h4zM3 17h3v2h12v-2h3v5H3z"/></svg>
    </div>
    <div class="util-item" style="left:394px">
      <div class="util-label">Our Brochure 2021</div>
      <div class="util-value">Download Now</div>
    </div>
    <div class="util-links">SERVICE REQUEST<span class="sep">|</span>NEWS FEED</div>
    <div class="icon-box" style="left:1074px">
      <svg width="14" height="14" viewBox="0 0 24 24"><circle cx="10" cy="10" r="6" fill="none" stroke="#fff" stroke-width="3"/><path d="M14.5 14.5l6 6" stroke="#fff" stroke-width="3.5" stroke-linecap="round"/></svg>
    </div>
  </div>

  <header class="site-header">
    <div class="brand"><span class="brand-mark"></span>VELMORA HOMECARE</div>
    <nav class="main-nav">
      <span>HOME</span><span class="sep">|</span>
      <span>ABOUT US</span><span class="sep">|</span>
      <span>SERVICES</span><span class="sep">|</span>
      <span>JOIN OUR TEAM</span><span class="sep">|</span>
      <span>TESTIMONIALS</span><span class="sep">|</span>
      <span>CONTACT US</span>
    </nav>
  </header>

  <section class="hero">
    <div class="hero-photo" role="img" aria-label="Photo of a smiling caregiver in a teal uniform hugging an elderly woman"></div>
    <h1 class="hero-title">
      <span class="line1">Special Care</span>
      <span class="line2">for your loved one</span>
      <span class="line3">everyday</span>
    </h1>
    <p class="hero-sub">Providing quality care services<br>for over 15 years</p>
    <div class="hero-button">SERVICE REQUEST</div>
  </section>
</body>
</html>
```